Business website cyber security

Full redesign of our current business website, mockup and powerpoint presentation have been provided.
Some animated elements (example: SVG with CSS) are welcome.
A detailed requirement list can also be found in the attached powerpoint
Also uploaded is the current page as a nicepage & html export. All 11 sites shall be reworked. "Branches", "Download", "Contact" and "Legal Information" are not needed .

A good example of a competitor is https://www.fennotrix.de/ this. Not in terms of colors, but in regard to website structure, animated elements and overall look.

Target Market(s)

Cyber security for the B2B market

Industry/Entity Type

IT, IT Security, banking

Coding

Coded - Design and coding required

Number of Pages Required

5+ page

Other font styles liked:
• ReadexPro Regular, ReadexPro Light

Colors
0054AA
0677BA
7BADD7
CADEEF
E8F1F8

Requirements
Must have
• Modern and sleek design, corporate identity
Nice to have
• Animated elements (css svg)
Should not have
• too many colors (max 4), too fancy

```html
<!DOCTYPE html>
<html lang="en">
<head>
<meta charset="utf-8">
<title>Korvane – IT Security &amp; Compliance</title>
<link href="https://fonts.googleapis.com/css2?family=Readex+Pro:wght@300;400;500;600&family=Oswald:wght@500&family=Arimo:wght@400;700&display=swap" rel="stylesheet">
<style>
:root{
  --brand-900:#0c1440;
  --brand-800:#1e1148;
  --brand-700:#23367f;
  --brand-600:#1d3b9e;
  --brand-500:#0054aa;
  --brand-400:#0677ba;
  --accent:#0b8fe0;
  --sky:#7badd7;
  --mist:#cadeef;
  --ice:#e8f1f8;
  --ink:#222;
  --muted:#666;
  --white:#fff;
}
*{box-sizing:border-box;margin:0;padding:0}
html,body{width:1200px;height:3509px;overflow:hidden}
body{position:relative;font-family:"Readex Pro",sans-serif;color:var(--ink);background:var(--white)}
.abs{position:absolute}
/* nav */
.topbar{left:0;top:0;width:1200px;height:91px;background:linear-gradient(90deg,#2b3f9f,#2e45a8);border-top:6px solid var(--accent)}
.nav-link{top:6px;height:85px;line-height:85px;color:var(--white);font-size:16px;text-decoration:none}
.lang{left:1073px;top:6px;width:56px;height:85px;background:var(--accent);color:#fff;font-size:15px;text-align:center;line-height:85px}
.brand-badge{border-radius:50%;background:#fff;border:4px solid var(--brand-500);display:flex;align-items:center;justify-content:center;gap:6px;color:var(--brand-500);font-weight:600;z-index:5}
.brand-badge .dot{width:10px;height:10px;background:var(--accent)}
/* hero */
.hero{left:0;top:91px;width:1200px;height:553px;background:#1f1450}
.hero-art{left:422px;top:0;width:778px;height:553px;background:radial-gradient(ellipse at 50% 50%,#2f7dff 0%,#3a3bd0 35%,#2a1a78 65%,#1f1450 100%);animation:glow 6s ease-in-out infinite alternate}
@keyframes glow{from{opacity:.85}to{opacity:1}}
.hero-title{left:99px;top:118px;width:430px;font-size:40px;font-weight:400;line-height:45px;color:#fff}
.hero-lead{left:99px;top:284px;width:305px;font-size:13.5px;line-height:17px;color:#fff}
.btn-read{left:97px;top:411px;width:130px;height:34px;border-radius:17px;background:linear-gradient(#1aa0ee,#0677ba);border:2px solid #5cc3ff;color:#fff;font-size:13px;font-weight:600;text-align:center;line-height:30px}
/* services */
.services{left:0;top:644px;width:1200px;height:273px;background:var(--brand-800)}
.svc{top:64px;width:316px;height:171px;border:1px solid #3b4fb3;border-radius:10px;background:#221a66;text-align:center;color:#fff}
.svc .ico{position:absolute;left:124px;top:-34px;width:68px;height:68px;border-radius:50%;background:#221a66;border:1px solid #3b4fb3;display:flex;align-items:center;justify-content:center}
.svc h3{margin-top:34px;font-size:18px;font-weight:500;color:var(--accent)}
.svc p{margin:18px auto 0;width:240px;font-size:13px;line-height:17px;font-weight:300}
/* headings */
.sec-title{left:0;width:1200px;text-align:center;font-size:40px;font-weight:500;color:var(--brand-600)}
.rule{left:565px;width:70px;height:3px;background:var(--accent)}
.rule::after{content:"";position:absolute;right:-2px;top:-4px;width:11px;height:11px;border-radius:50%;background:var(--accent)}
/* vision */
.vision{left:0;top:917px;width:1200px;height:606px;background:linear-gradient(120deg,#fff,#eef0f3 60%,#f5f6f8)}
.tabs{left:99px;top:1076px;width:1001px;height:57px;display:flex;border-radius:10px 10px 0 0;overflow:hidden;border:2px solid var(--brand-500)}
.tab{flex:1;text-align:center;line-height:53px;color:#fff;font-size:22px;background:var(--brand-600);border-left:1px solid #4f6ac8}
.tab.is-active{background:linear-gradient(#1aa0ee,#0677ba);border-left:none}
.tab-panel{left:99px;top:1131px;width:1001px;height:320px;background:#fff;border:2px solid var(--accent);border-top:none;border-radius:0 0 10px 10px}
.vision-art{left:154px;top:1150px;width:280px;height:280px;border-radius:50%;border:5px solid var(--accent);background:radial-gradient(circle at 50% 45%,#3d6bf0,#1a3ba8 70%);box-shadow:inset 0 0 0 8px #fff}
.vision-copy{left:480px;top:1165px;width:570px;font-size:15px;line-height:19px;color:#222}
.vision-copy h3{font-size:22px;font-weight:500;color:var(--brand-600);margin-bottom:16px}
.vision-copy b{font-weight:500}
/* sectors */
.sectors-band{left:0;top:1523px;width:1200px;height:357px;background:linear-gradient(90deg,#1a6fd0,#1d4fb8 50%,#2a3aa6)}
.sector{width:323px;height:313px;background:#f4f4f4;border:1px solid #ddd;border-bottom:4px solid #ccc}
.sector .photo{position:absolute;left:12px;top:12px;width:299px;height:200px}
.sector .badge{position:absolute;left:112px;top:144px;width:100px;height:100px;border-radius:50%;background:var(--brand-600);border:4px solid #fff;display:flex;align-items:center;justify-content:center}
.sector h4{position:absolute;left:0;top:257px;width:100%;text-align:center;font-family:"Oswald",sans-serif;font-weight:500;font-size:23px;color:#222;letter-spacing:.2px}
/* partners */
.partner{top:2482px;width:236px;height:107px;border:2px solid #d3d3d3;border-radius:10px;background:#fff;display:flex;align-items:center;justify-content:center}
.partner span{display:block;width:120px;height:30px;border-radius:6px;background:#e0e0e0}
.dots{left:565px;top:2615px;display:flex;gap:9px}
.dots i{width:12px;height:12px;border-radius:50%;border:2px solid #555}
.dots i.on{background:var(--accent);border-color:var(--accent)}
/* news */
.news{top:2780px;width:317px;height:353px;border:1px solid #ddd;background:#fff;font-family:"Arimo",sans-serif}
.news .photo{height:170px;position:relative}
.news .date{position:absolute;right:10px;top:8px;width:40px;height:40px;background:var(--accent);color:#fff;text-align:center;font-weight:700;font-size:16px;line-height:16px;padding-top:4px}
.news .date small{font-size:11px;display:block}
.news .meta{margin:30px 18px 0;font-size:14px;color:#666}
.news h5{margin:8px 18px 0;font-size:19px;color:var(--accent);font-weight:700}
.news p{margin:6px 18px 0;font-size:14px;line-height:17px;color:#666}
.news .foot{position:absolute;left:22px;right:22px;bottom:12px;display:flex;justify-content:space-between;font-size:14px;font-weight:700;color:#222}
/* footer */
.footer-band{left:0;top:3184px;width:1200px;height:325px;background:radial-gradient(ellipse at 50% 30%,#1a2a7a,var(--brand-900) 70%)}
.footer-legal{left:0;top:3358px;width:1200px;text-align:center;color:#fff;font-size:25px;font-weight:600;line-height:32px}
.footer-links{left:0;top:3401px;width:1200px;text-align:center;color:#fff;font-size:17px;line-height:22px}
.social{left:575px;top:3434px;width:52px;height:52px;border-radius:50%;background:var(--accent);border:3px solid #3b6fd0}
</style>
</head>
<body>

<header>
  <div class="abs topbar"></div>
  <a class="abs nav-link" style="left:116px" href="#">CDaaS</a>
  <a class="abs nav-link" style="left:206px" href="#">Security Services</a>
  <a class="abs nav-link" style="left:377px" href="#">Compliance</a>
  <a class="abs nav-link" style="left:726px" href="#">Our Company</a>
  <a class="abs nav-link" style="left:870px" href="#">Career</a>
  <a class="abs nav-link" style="left:959px" href="#">Contact Us</a>
  <div class="abs lang">EN &#8964;</div>
  <div class="abs brand-badge" style="left:518px;top:27px;width:164px;height:164px;font-size:28px"><i class="dot"></i>Korvane</div>
</header>

<section class="abs hero">
  <div class="abs hero-art" role="img" aria-label="Isometric illustration of a security shield in front of dashboards, screens and servers"></div>
  <h1 class="abs hero-title">The IT security of your IT infrastructure is our mission.</h1>
  <p class="abs hero-lead">Our cybersecurity services are designed around the customer. We offer a robust collaboration to understand the challenges of your environment and to develop tailor-made, secure solutions.</p>
  <a class="abs btn-read">Read More</a>
</section>

<section class="abs services">
  <div class="abs svc" style="left:99px">
    <div class="ico"><svg width="36" height="36" viewBox="0 0 36 36" fill="none" stroke="#fff" stroke-width="2"><circle cx="18" cy="18" r="7"/><path d="M18 4v7M18 25v7M4 18h7M25 18h7M8 8l5 5M23 23l5 5M28 8l-5 5M13 23l-5 5"/></svg></div>
    <h3>Cyber Defense as a Service</h3>
    <p>Our all-in-one CDaaS offer offers a convenient integration of your IT infrastructure into an active and comprehensive security solution.</p>
  </div>
  <div class="abs svc" style="left:443px">
    <div class="ico"><svg width="36" height="36" viewBox="0 0 36 36" fill="none" stroke="#fff" stroke-width="2"><circle cx="18" cy="18" r="15"/><rect x="12" y="16" width="12" height="10" rx="1"/><path d="M14 16v-3a4 4 0 0 1 8 0v3"/></svg></div>
    <h3>Security Services</h3>
    <p>Our security services provide you with comprehensive support in the planning and implementation of your holistic IT and information management.</p>
  </div>
  <div class="abs svc" style="left:785px">
    <div class="ico"><svg width="36" height="36" viewBox="0 0 36 36" fill="none" stroke="#fff" stroke-width="2"><path d="M9 4h14l5 5v23H9z"/><path d="M14 14h10M14 20h10M14 26h6"/></svg></div>
    <h3>Compliance</h3>
    <p>We support you with your IT security at the highest level with an effective compliance strategy.</p>
  </div>
</section>

<section>
  <div class="abs vision"></div>
  <h2 class="abs sec-title" style="top:958px">Vision &amp; Mission</h2>
  <div class="abs rule" style="top:1026px"></div>
  <div class="abs tabs"><div class="tab is-active">Vision</div><div class="tab">Mission</div><div class="tab">Portfolio</div></div>
  <div class="abs tab-panel"></div>
  <div class="abs vision-art" role="img" aria-label="Illustration of a server stack protected by a shield"></div>
  <div class="abs vision-copy">
    <h3>Holistic IT security is our claim.</h3>
    <p>We stand for your IT security. We offer extensive services and our certified IT experts work with you to ensure that your systems are secure.<br>With us you have:<br><b>• Fastest response times 24x7<br>• Market<br>leading technologies • Certified cyber analysts with the highest level of expertise</b></p>
    <p style="margin-top:19px">The "Pay-As-You-Grow" model allows ongoing adjustments to the professional security services used - with one claim: your needs.</p>
  </div>
</section>

<section>
  <div class="abs sectors-band"></div>
  <h2 class="abs sec-title" style="top:1560px;color:#fff">Industry Sectors</h2>
  <div class="abs rule" style="top:1627px"></div>

  <div class="abs sector" style="left:99px;top:1665px">
    <div class="photo" role="img" aria-label="Photo of finance icons over a hand on a dark blue background" style="background:linear-gradient(135deg,#1b3e6e,#0e1f3a)"></div>
    <div class="badge"><svg width="46" height="46" viewBox="0 0 46 46" fill="none" stroke="#fff" stroke-width="3"><path d="M10 6h18l6 6v28H10z"/><circle cx="32" cy="32" r="8" fill="#1d3b9e"/><path d="M16 28v-6M21 28v-10M26 28v-4"/></svg></div>
    <h4>FINANCIAL</h4>
  </div>
  <div class="abs sector" style="left:437px;top:1665px">
    <div class="photo" role="img" aria-label="Photo of scales of justice and a gavel on a desk" style="background:linear-gradient(135deg,#6a5a46,#2c2620)"></div>
    <div class="badge"><svg width="46" height="46" viewBox="0 0 46 46" fill="#fff"><path d="M23 5 5 14v4h36v-4z"/><rect x="9" y="20" width="5" height="14"/><rect x="20.5" y="20" width="5" height="14"/><rect x="32" y="20" width="5" height="14"/><rect x="5" y="36" width="36" height="5"/></svg></div>
    <h4>GOVERNORATE</h4>
  </div>
  <div class="abs sector" style="left:775px;top:1665px">
    <div class="photo" role="img" aria-label="Photo of a control room with many monitors" style="background:linear-gradient(135deg,#2a5f8c,#0d2238)"></div>
    <div class="badge"><svg width="46" height="46" viewBox="0 0 46 46" fill="none" stroke="#fff" stroke-width="4" stroke-linecap="round"><path d="M12 34 34 12M18 14l14 18M10 38l6-6"/></svg></div>
    <h4>ARROWSPACE/ AVIATION</h4>
  </div>
  <div class="abs sector" style="left:99px;top:1993px">
    <div class="photo" role="img" aria-label="Photo of a person holding a tablet in a warehouse" style="background:linear-gradient(135deg,#2d5572,#1a2a3a)"></div>
    <div class="badge"><svg width="46" height="46" viewBox="0 0 46 46" fill="#fff"><rect x="5" y="12" width="22" height="18" rx="2"/><path d="M29 18h7l5 6v6H29z"/><circle cx="13" cy="34" r="4"/><circle cx="34" cy="34" r="4"/></svg></div>
    <h4>LOGISTICS</h4>
  </div>
  <div class="abs sector" style="left:437px;top:1993px">
    <div class="photo" role="img" aria-label="Photo of engineers looking at a car design on screens" style="background:linear-gradient(135deg,#3a5a78,#131f2d)"></div>
    <div class="badge"><svg width="46" height="46" viewBox="0 0 46 46" fill="#fff"><path d="M10 22l4-9h18l4 9v12H10z"/><rect x="11" y="34" width="6" height="5"/><rect x="29" y="34" width="6" height="5"/><circle cx="16" cy="27" r="2.5" fill="#1d3b9e"/><circle cx="30" cy="27" r="2.5" fill="#1d3b9e"/></svg></div>
    <h4>AUTOMOTIVE</h4>
  </div>
  <div class="abs sector" style="left:775px;top:1993px">
    <div class="photo" role="img" aria-label="Photo of a hand touching a glowing cloud interface" style="background:linear-gradient(135deg,#3d8fd0,#1b4d8a)"></div>
    <div class="badge"><svg width="46" height="46" viewBox="0 0 46 46" fill="none" stroke="#fff" stroke-width="3"><path d="M38 23a15 15 0 0 1-26 10M8 23a15 15 0 0 1 26-10"/><path d="M34 6v7h-7M12 40v-7h7"/><path d="M25 12l-6 12h8l-6 11" stroke-linejoin="round"/></svg></div>
    <h4>ENERGY &amp; CHEMISTRY</h4>
  </div>
</section>

<section>
  <h2 class="abs sec-title" style="top:2370px">Products &amp; Partners</h2>
  <div class="abs rule" style="top:2437px"></div>
  <div class="abs partner" style="left:99px" aria-label="Partner badge"><span></span></div>
  <div class="abs partner" style="left:354px" aria-label="Partner badge"><span></span></div>
  <div class="abs partner" style="left:610px" aria-label="Partner badge"><span></span></div>
  <div class="abs partner" style="left:866px" aria-label="Partner badge"><span></span></div>
  <div class="abs dots"><i class="on"></i><i></i><i></i><i></i></div>
</section>

<section>
  <h2 class="abs sec-title" style="top:2682px">Latest News</h2>
  <div class="abs rule" style="top:2749px"></div>

  <article class="abs news" style="left:98px">
    <div class="photo" role="img" aria-label="Photo of two business people walking outdoors" style="background:linear-gradient(135deg,#8c8c84,#3c3a36)"><div class="date">30<small>JUN</small></div></div>
    <div class="meta">by admin | Latest Blog</div>
    <h5>LOREM IPSUM IS SIMPLY</h5>
    <p>Lorem Ipsum is simply dummy text of the printing and typesetting industry.</p>
    <div class="foot"><span>READ MORE</span><span>&#9633; 0 comment</span></div>
  </article>
  <article class="abs news" style="left:441px">
    <div class="photo" role="img" aria-label="Blue tinted photo of a city skyline" style="background:linear-gradient(#27a3ec,#1590dc)">
      <svg class="abs" style="left:138px;top:65px" width="40" height="40" viewBox="0 0 40 40"><circle cx="20" cy="20" r="19" fill="#fff"/><path d="M16 24l8-8M14 20l-2 2a4 4 0 0 0 6 6l2-2M26 20l2-2a4 4 0 0 0-6-6l-2 2" fill="none" stroke="#1590dc" stroke-width="2.5" stroke-linecap="round"/></svg>
    </div>
    <div class="meta">by admin | Latest Blog</div>
    <h5>LOREM IPSUM IS SIMPLY</h5>
    <p>Lorem Ipsum is simply dummy text of the printing and typesetting industry.</p>
    <div class="foot"><span>READ MORE</span><span>&#9633; 0 comment</span></div>
  </article>
  <article class="abs news" style="left:785px">
    <div class="photo" role="img" aria-label="Photo of an office worker at a desk" style="background:linear-gradient(135deg,#b8b8b4,#5a5853)"><div class="date">30<small>JUN</small></div></div>
    <div class="meta">by admin | Latest Blog</div>
    <h5>LOREM IPSUM IS SIMPLY</h5>
    <p>Lorem Ipsum is simply dummy text of the printing and typesetting industry.</p>
    <div class="foot"><span>READ MORE</span><span>&#9633; 0 comment</span></div>
  </article>
</section>

<footer>
  <div class="abs footer-band"></div>
  <div class="abs brand-badge" style="left:529px;top:3205px;width:142px;height:142px;font-size:24px"><i class="dot"></i>Korvane</div>
  <div class="abs footer-legal">© Korvane (S.À RL) • TEL.: +352 2710 55 30 - 30</div>
  <div class="abs footer-links">• Contact • Imprint • Privacy • Legal Notice</div>
  <a class="abs social" href="#" aria-label="Social profile"></a>
</footer>

</body>
</html>
```